Design and format my book using Vantoro.com

The job would be to take the text and illustrations I supply and (using Vantoro.com) create an attractive book by formatting my stuff, using a suitable handwriting font for the text, sizing and placing images according to the formatting specs of the book, and using Vantoro's built-in apps to design an attractive cover. The style of font for the text of the book would be handwriting, something like this book: http://quillfern.net/shop/88-painters-to-sketch-along-with-on-trains/ except that my book will be in black and white. The illustrations have been done by my six year old colleague. We're excited to see what you come up with. Thank you.

Target Market(s)

mainstream, gift shop clientele

Font styles to use
Other font styles liked:
• see brief - handwriting as in example: http://quillfern.net/shop/88-painters-to-sketch-along-with-on-trains/

Colors
9bcb3c
ffffff
1b1b1b
959595
e8e8e8
cadf82
f78f20

Requirements
Must have
• an original book cover design, provided by the designer, formatted within the Vantoro.com App at their website (this means you will need to open a project at Vantoro.com and allow me to 'own' it when completed.
Nice to have
• Book should be in smaller format (envisioned as a novelty book of the kind you buy near the point of sale, intended as a low-price gift item or for its niche Irish market or the general public.
Should not have
• serious fonts

```html
<!DOCTYPE html>
<html lang="en">
<head>
<meta charset="utf-8">
<title>Emerald Firebrands – Spread 3–4</title>
<link href="https://fonts.googleapis.com/css2?family=Shadows+Into+Light+Two&display=swap" rel="stylesheet">
<style>
  :root {
    --paper: #ffffff;
    --ink: #1b1b1b;
    --ink-soft: #959595;
    --illustration-fill: #e8e8e8;
  }
  html, body {
    margin: 0;
    padding: 0;
    width: 1200px;
    height: 851px;
    overflow: hidden;
    background: var(--paper);
  }
  .spread {
    position: relative;
    width: 1200px;
    height: 851px;
    background: var(--paper);
    color: var(--ink);
    font-family: "Shadows Into Light Two", cursive;
  }
  .profile-text {
    position: absolute;
    left: 48px;
    top: 105px;
    width: 520px;
    font-size: 14.6px;
    line-height: 24.8px;
    letter-spacing: 0.15px;
  }
  .profile-text .line {
    display: block;
    white-space: nowrap;
  }
  .profile-text .loose { line-height: 28.8px; }
  .profile-text .gap { margin-top: 5px; }
  .profile-text .gap-large { margin-top: 10px; }
  .profile-name {
    font-size: 16px;
    letter-spacing: 0.5px;
    text-transform: uppercase;
    font-weight: 400;
    -webkit-text-stroke: 0.5px var(--ink);
  }
  .illustration {
    position: absolute;
    left: 684px;
    top: 284px;
    width: 436px;
    height: 268px;
    background: var(--illustration-fill);
  }
  .running-footer {
    position: absolute;
    left: 48px;
    top: 772px;
    font-size: 5px;
    letter-spacing: 0.3px;
    color: var(--ink);
    text-transform: uppercase;
    white-space: nowrap;
  }
  .page-number {
    position: absolute;
    top: 820px;
    font-size: 12px;
    color: var(--ink-soft);
  }
  .page-number.left { left: 282px; }
  .page-number.right { left: 882px; }
</style>
</head>
<body>
<main class="spread">
  <article class="profile-text">
    <span class="line"><span class="profile-name">Maeve-Rose Kilbride</span> At only nine years old, Irish ninja warrior Maeve Rose</span>
    <span class="line">Kilbride took the world by storm when she exhibited her astonishing martial arts</span>
    <span class="line">skills on Stars of the Isles, Series 9.</span>
    <span class="line">The judges and audience were stunned by her masterful Samurai swordsmanship,</span>
    <span class="line">acrobatics and lightening-fast choreography. She ended her performance with a</span>
    <span class="line">front flip and an exuberant roar. She sailed into the next round with Desmond Harrow</span>
    <span class="line">jokingly offering her a job as his personal security guard. In the semi-final</span>
    <span class="line">she entered the stage wearing a red dress and hood, and her performance this</span>
    <span class="line">time involved her "fighting off" Ninja warriors with her sword. In the final, her</span>
    <span class="line">performance was styled as a 'computer game' in which she fought off a number of</span>
    <span class="line">fictional characters. She placed eighth in the grand final, having by then won a</span>
    <span class="line">huge public following. Kilbride has capitalised on her talent by acting in films,</span>
    <span class="line">such as The Little Blade, as well as appearing on the Nora Quill show.</span>
    <span class="line">Kilbride grew up in County Armagh, Northern Ireland, where she tried ballet,</span>
    <span class="line">Irish dancing and basketball before finding her real calling in martial arts.</span>
    <span class="line loose gap">She also practices kickboxing, Kung Fu and Tae Kwon Do. She has competed and</span>
    <span class="line loose">won awards all over the world. She trains intensively in Ireland with her coach,</span>
    <span class="line loose">sensei Liam Fenwick. If you haven't already seen it, don't miss her stunning first</span>
    <span class="line loose">appearance on Stars of the Isles here:</span>
    <span class="line loose">https://www.clipwell.tv/watch?v=kT4rWm8QzPa</span>
    <span class="line gap-large">This clip always provides a little inspiration or, if you're feeling depressed at</span>
    <span class="line">the endless "Princess" images churned out in our culture, repeating the message</span>
    <span class="line">that girls should be "pretty" rather than athletic or powerful, Kilbride's video</span>
    <span class="line">furnishes the perfect antidote to that shit.</span>
  </article>

  <div class="illustration" role="img" aria-label="Black ink line drawing of a young martial artist doing the splits while raising a sword overhead"></div>

  <footer class="running-footer">Emerald Firebrands: 14 Fearless Sheros &amp; Heros to meet before you grow up by Orla Finnegan</footer>
  <span class="page-number left">3</span>
  <span class="page-number right">4</span>
</main>
</body>
</html>
```